Hollow and Hearth Wine Label Refresh

We have been using the same design on our hollow & hearth wine labels for years. We need to refresh the label with the same name, but an all new design that is more bold, eye catching, and that says "Michigan." We make wine in Michigan, and would like to see the label incorporate something to do with our state. The design should be playful, but not crude. We like to play up the names in an appropriate way.

Target Market(s)

Grocery store shoppers, mostly female

Requirements
Must have
• We make 4 wines, Hollow Red, Hearth Red, Hollow White, Hearth White. The red and white Hollow labels can have the same design, just different colors, and same for the Hearth Red and white. It is a set of 4. Please use the current shape of the label and place mock ups on red wine for the reds and white wines for the whites.
Should not have
• Inappropriate images

```html
<!DOCTYPE html>
<html lang="en">
<head>
<meta charset="utf-8">
<title>Hollow and Hearth Wine Labels</title>
<link rel="stylesheet" href="https://fonts.googleapis.com/css2?family=Oranienbaum&family=Oswald:wght@400;500;600&display=swap">
<style>
  :root {
    --red: #d9261c;
    --green: #2a8a3a;
    --lime: #8cc63f;
    --ink: #1b1b1b;
    --paper: #ffffff;
    --backdrop: #ececec;
    --flourish: #b9b9b9;
  }
  * { box-sizing: border-box; margin: 0; padding: 0; }
  html, body { width: 1200px; height: 1000px; overflow: hidden; }
  body {
    background: var(--backdrop);
    font-family: "Oswald", sans-serif;
    color: var(--ink);
  }
  .label-set {
    display: grid;
    grid-template-columns: repeat(4, 250px);
    column-gap: 40px;
    justify-content: center;
    padding-top: 150px;
  }
  .wine { --accent: var(--red); }
  .wine--green { --accent: var(--green); }
  .wine--lime { --accent: var(--lime); }

  /* neck collar */
  .neck {
    width: 130px;
    height: 150px;
    margin: 0 auto 50px;
    background: var(--paper);
    border-radius: 6px 6px 0 0;
    position: relative;
    display: flex;
    flex-direction: column;
    align-items: center;
    padding-top: 34px;
  }
  .neck::after {
    content: "";
    position: absolute;
    left: 0; right: 0; bottom: 0;
    height: 5px;
    background: var(--ink);
    box-shadow: 0 -4px 0 -2px var(--paper), 0 -5px 0 -2px var(--ink);
  }
  .neck .brand { font-size: 10px; margin-bottom: 36px; }

  .brand {
    display: flex;
    align-items: center;
    gap: 5px;
    color: var(--accent);
    font-weight: 600;
    letter-spacing: 0.14em;
    text-transform: uppercase;
    white-space: nowrap;
  }
  .brand__dot {
    width: 9px; height: 9px;
    border-radius: 50%;
    background: var(--accent);
  }
  .pill {
    display: inline-block;
    background: var(--accent);
    color: var(--paper);
    font-size: 9px;
    font-weight: 500;
    letter-spacing: 0.04em;
    line-height: 1;
    padding: 3px 8px;
    border-radius: 8px;
    text-transform: uppercase;
  }

  /* front label */
  .label {
    position: relative;
    width: 250px;
    height: 340px;
    text-align: center;
  }
  .label__frame { position: absolute; inset: 0; }
  .label__frame .sheet { fill: var(--paper); }
  .label__frame .rule-outer { fill: none; stroke: var(--accent); stroke-width: 2; }
  .label__frame .rule-inner { fill: none; stroke: var(--accent); stroke-width: 0.8; }
  .label__content {
    position: relative;
    display: flex;
    flex-direction: column;
    align-items: center;
    padding-top: 52px;
    height: 100%;
  }
  .label__masthead {
    display: flex;
    align-items: center;
    gap: 10px;
    height: 40px;
  }
  .label__masthead .brand { font-size: 11px; }
  .flourish {
    width: 30px;
    height: 8px;
    border-radius: 4px;
    background: var(--flourish);
  }
  .label__name {
    font-family: "Oranienbaum", serif;
    color: var(--accent);
    text-transform: uppercase;
    line-height: 1;
    margin-top: 44px;
    height: 48px;
    display: flex;
    align-items: flex-end;
    white-space: nowrap;
  }
  .label__name--hollow { font-size: 31px; }
  .label__name--hearth { font-size: 38px; }
  .label__region {
    margin-top: 10px;
    display: grid;
    grid-template-columns: 38px auto 38px;
    align-items: center;
    column-gap: 8px;
    font-size: 13px;
    font-weight: 500;
    line-height: 1.05;
    letter-spacing: 0.06em;
    text-transform: uppercase;
  }
  .rules {
    height: 11px;
    border-top: 1px solid var(--ink);
    border-bottom: 1px solid var(--ink);
    position: relative;
  }
  .rules::after {
    content: "";
    position: absolute;
    left: 0; right: 0; top: 4px;
    border-top: 1px solid var(--ink);
  }
  .label .pill { margin-top: 40px; }
  .label__abv {
    margin-top: 34px;
    font-size: 7px;
    font-weight: 500;
    letter-spacing: 0.03em;
    text-transform: uppercase;
  }
</style>
</head>
<body>
<main class="label-set">

  <article class="wine wine--red">
    <div class="neck">
      <div class="brand"><span class="brand__dot"></span>Domaine Alder</div>
      <span class="pill">Dry</span>
    </div>
    <section class="label">
      <svg class="label__frame" viewBox="0 0 250 340" aria-hidden="true">
        <path class="sheet" d="M0 34 Q125 -6 250 34 L250 340 L0 340 Z"/>
        <path class="rule-outer" d="M10 42 Q125 6 240 42 L240 330 L10 330 Z"/>
        <path class="rule-inner" d="M15 47 Q125 12 235 47 L235 325 L15 325 Z"/>
      </svg>
      <div class="label__content">
        <div class="label__masthead">
          <span class="flourish" role="img" aria-label="scroll flourish"></span>
          <div class="brand"><span class="brand__dot"></span>Domaine Alder</div>
          <span class="flourish" role="img" aria-label="scroll flourish"></span>
        </div>
        <h2 class="label__name label__name--hollow">Hollow Red</h2>
        <div class="label__region"><span class="rules"></span><span>Old Mission<br>Peninsula</span><span class="rules"></span></div>
        <span class="pill">Dry</span>
        <p class="label__abv">Alcohol 12.5% by volume</p>
      </div>
    </section>
  </article>

  <article class="wine wine--red">
    <div class="neck">
      <div class="brand"><span class="brand__dot"></span>Domaine Alder</div>
      <span class="pill">Semi-Sweet</span>
    </div>
    <section class="label">
      <svg class="label__frame" viewBox="0 0 250 340" aria-hidden="true">
        <path class="sheet" d="M0 34 Q125 -6 250 34 L250 340 L0 340 Z"/>
        <path class="rule-outer" d="M10 42 Q125 6 240 42 L240 330 L10 330 Z"/>
        <path class="rule-inner" d="M15 47 Q125 12 235 47 L235 325 L15 325 Z"/>
      </svg>
      <div class="label__content">
        <div class="label__masthead">
          <span class="flourish" role="img" aria-label="scroll flourish"></span>
          <div class="brand"><span class="brand__dot"></span>Domaine Alder</div>
          <span class="flourish" role="img" aria-label="scroll flourish"></span>
        </div>
        <h2 class="label__name label__name--hearth">Hearth Red</h2>
        <div class="label__region"><span class="rules"></span><span>Old Mission<br>Peninsula</span><span class="rules"></span></div>
        <span class="pill">Semi-Sweet</span>
        <p class="label__abv">Alcohol 12.5% by volume</p>
      </div>
    </section>
  </article>

  <article class="wine wine--green">
    <div class="neck">
      <div class="brand"><span class="brand__dot"></span>Domaine Alder</div>
      <span class="pill">Dry</span>
    </div>
    <section class="label">
      <svg class="label__frame" viewBox="0 0 250 340" aria-hidden="true">
        <path class="sheet" d="M0 34 Q125 -6 250 34 L250 340 L0 340 Z"/>
        <path class="rule-outer" d="M10 42 Q125 6 240 42 L240 330 L10 330 Z"/>
        <path class="rule-inner" d="M15 47 Q125 12 235 47 L235 325 L15 325 Z"/>
      </svg>
      <div class="label__content">
        <div class="label__masthead">
          <span class="flourish" role="img" aria-label="scroll flourish"></span>
          <div class="brand"><span class="brand__dot"></span>Domaine Alder</div>
          <span class="flourish" role="img" aria-label="scroll flourish"></span>
        </div>
        <h2 class="label__name label__name--hollow">Hollow White</h2>
        <div class="label__region"><span class="rules"></span><span>Old Mission<br>Peninsula</span><span class="rules"></span></div>
        <span class="pill">Dry</span>
        <p class="label__abv">Alcohol 12.5% by volume</p>
      </div>
    </section>
  </article>

  <article class="wine wine--lime">
    <div class="neck">
      <div class="brand"><span class="brand__dot"></span>Domaine Alder</div>
      <span class="pill">Semi-Sweet</span>
    </div>
    <section class="label">
      <svg class="label__frame" viewBox="0 0 250 340" aria-hidden="true">
        <path class="sheet" d="M0 34 Q125 -6 250 34 L250 340 L0 340 Z"/>
        <path class="rule-outer" d="M10 42 Q125 6 240 42 L240 330 L10 330 Z"/>
        <path class="rule-inner" d="M15 47 Q125 12 235 47 L235 325 L15 325 Z"/>
      </svg>
      <div class="label__content">
        <div class="label__masthead">
          <span class="flourish" role="img" aria-label="scroll flourish"></span>
          <div class="brand"><span class="brand__dot"></span>Domaine Alder</div>
          <span class="flourish" role="img" aria-label="scroll flourish"></span>
        </div>
        <h2 class="label__name label__name--hearth" style="font-size:34px">Hearth White</h2>
        <div class="label__region"><span class="rules"></span><span>Old Mission<br>Peninsula</span><span class="rules"></span></div>
        <span class="pill">Semi-Sweet</span>
        <p class="label__abv">Alcohol 12.5% by volume</p>
      </div>
    </section>
  </article>

</main>
</body>
</html>
```